Real Estate Agent needs business card design

We have logo designed already, want to have business card designed. Very interested in those smaller size business card as they look very trendy. Business name is called VORENDA REALTY

```html
<!DOCTYPE html>
<html lang="en">
<head>
<meta charset="utf-8">
<title>Vorenda Realty – Business Cards</title>
<link rel="stylesheet" href="https://fonts.googleapis.com/css2?family=Cinzel:wght@400&family=Open+Sans:wght@400;600&display=swap">
<style>
  :root {
    --backdrop: #3a3330;
    --card: #141414;
    --card-edge: #1f1f1f;
    --gold: #b38f5f;
    --ink: #f2f2f2;
    --muted: #9a9a9a;
    --rule: #cfcfcf;
  }
  * { margin: 0; padding: 0; box-sizing: border-box; }
  html, body { width: 1200px; height: 864px; overflow: hidden; }
  body {
    background: var(--backdrop);
    position: relative;
    font-family: "Open Sans", Arial, sans-serif;
  }
  .card {
    position: absolute;
    width: 540px;
    height: 309px;
    background: linear-gradient(160deg, var(--card-edge), var(--card) 60%);
    box-shadow: 0 18px 40px rgba(0,0,0,.45);
  }
  .card--front { left: 50px; top: 110px; }
  .card--back { left: 610px; top: 445px; }

  .brand { display: flex; flex-direction: column; align-items: center; }
  .brand__mark { width: 34px; height: 34px; background: var(--gold); margin-bottom: 14px; }
  .brand__name {
    font-family: "Cinzel", Georgia, serif;
    font-weight: 400;
    color: var(--ink);
    letter-spacing: 1px;
    white-space: nowrap;
  }

  .card--front .brand { position: absolute; left: 0; right: 0; top: 82px; }
  .card--front .brand__name { font-size: 34px; color: #d8d8d8; }
  .front__web {
    position: absolute; left: 0; right: 0; top: 210px;
    text-align: center; color: var(--muted);
    font-size: 12px; letter-spacing: 5px;
  }

  .card--back .brand { position: absolute; left: 20px; width: 280px; top: 100px; }
  .card--back .brand__name { font-size: 28px; }
  .back__rule {
    position: absolute; left: 310px; top: 40px; width: 1px; height: 229px;
    background: linear-gradient(to bottom, transparent, var(--rule) 30%, var(--rule) 70%, transparent);
  }
  .contact { position: absolute; left: 328px; top: 58px; color: var(--ink); font-size: 13px; line-height: 19px; }
  .contact__name { color: var(--gold); font-weight: 600; letter-spacing: .5px; }
  .contact__role { margin-bottom: 2px; }
  .contact__line { display: flex; align-items: center; gap: 7px; }
  .contact__line svg { width: 11px; height: 11px; fill: var(--gold); flex: none; }
</style>
</head>
<body>
  <section class="card card--front">
    <div class="brand">
      <div class="brand__mark"></div>
      <div class="brand__name">VORENDA REALTY</div>
    </div>
    <div class="front__web">www.vorendarealty.com</div>
  </section>

  <section class="card card--back">
    <div class="brand">
      <div class="brand__mark"></div>
      <div class="brand__name">VORENDA REALTY</div>
    </div>
    <div class="back__rule"></div>
    <div class="contact">
      <div class="contact__name">DANIEL HART</div>
      <div class="contact__role">CEO/FOUNDER</div>
      <div>4120 Birchwood Lane</div>
      <div>Juneau, Alaska 99801</div>
      <div class="contact__line">
        <svg viewBox="0 0 12 12"><path d="M2 1h3l1 3-1.5 1a6 6 0 0 0 2.5 2.5L8 6l3 1v3a1 1 0 0 1-1 1A9 9 0 0 1 1 2a1 1 0 0 1 1-1z"/></svg>
        <span>555 214 7830</span>
      </div>
      <div class="contact__line">
        <svg viewBox="0 0 12 12"><path d="M3 0h6a1 1 0 0 1 1 1v10a1 1 0 0 1-1 1H3a1 1 0 0 1-1-1V1a1 1 0 0 1 1-1zm0 2v7h6V2z"/></svg>
        <span>555 382 6419</span>
      </div>
      <div class="contact__line">
        <svg viewBox="0 0 12 12"><path d="M3 0h5v3H3zM1 4h10v5H9v3H3V9H1zm3 5v2h4V9z"/></svg>
        <span>555 907 1526</span>
      </div>
      <div class="contact__line">
        <svg viewBox="0 0 12 12"><path d="M0 2h12v1L6 7 0 3zm0 2.5 6 4 6-4V10H0z"/></svg>
        <span>daniel@vorendarealty.com</span>
      </div>
      <div class="contact__line">
        <svg viewBox="0 0 12 12"><circle cx="6" cy="6" r="5.5"/></svg>
        <span>www.vorendarealty.com</span>
      </div>
    </div>
  </section>
</body>
</html>
```